Website redesign for Maplecrest Drip Clinic

We need website redesign for Maplecrest Drip Clinic - Natural Health & Wellness Center.
In addition to our IV Infusions & Intramuscular Injection, our team offers a full spectrum of natural healing modalities to optimize physical, emotional and spiritual well being.
our current website is www.maplecrestdripcare.com
Our major competitor is https://brisknookhydra.com/
See uploaded design of current logo.
Target Market(s)
Health, fitness, functional medicine, immune boosting, alternative medicine, holistic medicine, supplements
Industry/Entity Type
Health And Wellness
Logo Text
Maplecrest Drip Clinic - Natural Health & Wellness Center
Number of Pages Required
5+ page
Requirements
Must have
- Contemporary Professional / Medical / Health Professional Look
Our current website is www.maplecrestdripcare.com

```html
<!DOCTYPE html>
<html lang="en">
<head>
<meta charset="utf-8">
<title>Maplecrest Drip Clinic - Natural Health &amp; Wellness Center</title>
<link href="https://fonts.googleapis.com/css2?family=Lato:wght@300;400;700&family=Tinos:wght@400&display=swap" rel="stylesheet">
<style>
:root{
  --navy:#2b3566;
  --ink:#1c1c1c;
  --muted:#6a6f78;
  --green:#a6e23c;
  --green-text:#a6d93a;
  --blue:#0575a6;
  --blue-deep:#034b83;
  --teal:#3ba9bd;
  --band:#0a4d88;
  --footer:#262626;
  --hero-bg:#e3e6ec;
}
*{margin:0;padding:0;box-sizing:border-box}
html,body{width:1200px;height:4382px;overflow:hidden;background:#fff}
body{position:relative;font-family:"Lato",sans-serif;color:var(--ink)}
.abs{position:absolute}

.site-header{position:absolute;left:0;top:0;width:1200px;height:65px;background:#fff;border-bottom:1px solid #e6e6e6}
.brand{position:absolute;left:50px;top:20px;display:flex;align-items:center;gap:8px;font-size:16px;font-weight:700;color:var(--navy)}
.brand-dot{width:22px;height:22px;border-radius:50%;background:var(--navy)}
.main-nav{position:absolute;right:40px;top:24px;display:flex;gap:20px;font-size:15px;color:#222}

.hero{position:absolute;left:0;top:65px;width:1200px;height:623px;background:linear-gradient(90deg,#e6e9ee 0%,#dde1e8 50%,#cfd5de 100%)}
.hero-photo{position:absolute;right:0;top:0;width:560px;height:623px;background:radial-gradient(ellipse at 60% 45%,#b9c4d4 0%,#d2d8e1 45%,rgba(221,225,232,0) 75%)}
.hero h1{position:absolute;left:50px;top:126px;font-weight:400;font-size:37px;line-height:50px;color:#111}
.hero p{position:absolute;left:50px;top:245px;width:520px;font-size:17px;line-height:29px;color:#222}
.btn-session{position:absolute;left:46px;top:371px;width:209px;height:52px;background:var(--navy);color:#fff;border-radius:4px;font-size:19px;display:flex;align-items:center;justify-content:center}

.section-title{position:absolute;left:0;width:1200px;text-align:center;font-weight:400;font-size:44px;color:#111}

.slide-photo{position:absolute;left:63px;top:841px;width:539px;height:808px;background:linear-gradient(180deg,#cfcfcf 0%,#bdbdbd 50%,#9a9a9a 100%)}
.slide-text{position:absolute;left:642px;top:835px;width:480px}
.slide-text h3{font-weight:400;font-size:32px;letter-spacing:4px;color:#111}
.slide-text .tagline{margin-top:12px;font-size:22px;letter-spacing:3px;line-height:29px;color:var(--green-text)}
.slide-text .body{font-family:"Tinos",serif;font-size:19px;line-height:26px;color:#222}
.slide-text .intro{margin-top:14px}
.slide-text ul{list-style:none;margin:18px 0 0 20px}
.slide-text .inside{margin-top:20px}
.slide-text .ing{margin-top:14px;color:var(--green-text)}
.slide-text .ing + .body{margin-top:0}
.btn-book{position:absolute;left:642px;top:1700px;width:180px;height:48px;background:var(--green);border-radius:4px;font-size:22px;color:#1e3a1e;display:flex;align-items:center;justify-content:center}
.arrow{position:absolute;top:1160px}
.dots{position:absolute;left:494px;top:1811px;display:flex;gap:10px}
.dots span{width:24px;height:24px;border:2px solid #333;border-radius:50%}
.dots .on{background:var(--green);border-color:var(--green)}

.packages{position:absolute;left:75px;top:1954px;width:1038px;height:412px;display:flex}
.pkg{flex:1;background:var(--blue);color:#fff;padding:30px 0 0 32px;position:relative}
.pkg.featured{background:var(--blue-deep);padding-top:12px}
.pkg h4{font-weight:400;font-size:27px;margin-top:14px}
.pkg ul{list-style:none;margin:14px 0 0 20px;font-size:14px;line-height:32px}
.pkg .link{position:absolute;left:32px;bottom:44px;font-size:14px;padding-bottom:6px;border-bottom:1.5px solid #fff;width:116px}

.care-title{color:var(--navy);font-size:41px;top:2462px}
.care-intro{position:absolute;left:140px;top:2560px;width:920px;font-family:"Tinos",serif;font-size:16px;line-height:26px;color:#222}

.service{position:absolute;width:260px;text-align:center}
.service svg{display:block;margin:0 auto}
.service h5{font-weight:400;font-size:18px;letter-spacing:.5px;color:#222;margin-top:14px}
.service h5.linked{text-decoration:underline}
.service p{font-size:13px;line-height:18px;color:var(--muted);margin:40px auto 0;width:240px}

.newsletter{position:absolute;left:0;top:4025px;width:1200px;height:184px;background:var(--band)}
.newsletter h2{position:absolute;left:58px;top:70px;font-weight:400;font-size:40px;color:#fff}
.email-field{position:absolute;left:541px;top:72px;width:360px;height:49px;border:2px solid #fff;color:#fff;font-size:14px;padding-left:22px;display:flex;align-items:center}
.join-btn{position:absolute;left:901px;top:72px;width:217px;height:49px;background:var(--green);color:#1e3a1e;font-size:14px;display:flex;align-items:center;justify-content:center}

.site-footer{position:absolute;left:0;top:4209px;width:1200px;height:173px;background:var(--footer);color:#fff;font-family:"Tinos",serif;font-size:21px;line-height:32px}
.footer-col{position:absolute}
.footer-rule{position:absolute;top:28px;width:2px;height:140px;background:#fff}
</style>
</head>
<body>

<header class="site-header">
  <div class="brand"><span class="brand-dot"></span>Maplecrest Drip Clinic</div>
  <nav class="main-nav"><span>HOME</span><span>SERVICES</span><span>INTAKE FORMS</span><span>PRODUCTS</span><span>OUR TEAM</span><span>BOOK ONLINE</span><span>CONTACT US</span></nav>
</header>

<section class="hero">
  <div class="hero-photo" role="img" aria-label="Hand holding an IV bag filled with fresh fruit slices"></div>
  <h1>WELCOME TO MAPLECREST DRIP CLINIC<br>NATURAL HEALTH &amp; WELLNESS</h1>
  <p>Our team offers a full spectrum of healing modalities to optimize your physical, emotional and spiritual well being. Check out our list of treatments and services below.</p>
  <div class="btn-session">BOOK A SESSION</div>
</section>

<h2 class="section-title" style="top:730px">IV INFUSION MENU</h2>

<svg class="arrow" style="left:14px" width="50" height="100" viewBox="0 0 50 100"><path d="M40 6 L10 50 L40 94" fill="none" stroke="#c8c8c8" stroke-width="12"/></svg>
<svg class="arrow" style="left:1132px" width="50" height="100" viewBox="0 0 50 100"><path d="M10 6 L40 50 L10 94" fill="none" stroke="#c8c8c8" stroke-width="12"/></svg>

<div class="slide-photo" role="img" aria-label="Young man in a cap holding his hand to his face in discomfort"></div>
<div class="slide-text">
  <h3>ALLEVIATE PMS | $150</h3>
  <div class="tagline">REDUCE BLOATING, IRRITABILITY, ABDOMINAL DISCOMFORT AND MORE</div>
  <p class="body intro">Compounded to help relieve symptoms of PMS, this customized drip includes premium-quality compounds which may reduce bloating, irritability, abdominal discomfort and lower back pain.</p>
  <ul class="body">
    <li>-Helps minimize bloating</li>
    <li>-Reduces abdominal discomfort</li>
    <li>-Improves irritability</li>
    <li>-Helps decrease lower back pain</li>
  </ul>
  <p class="body inside">What's inside:</p>
  <p class="body ing">B-Complex Vitamins</p>
  <p class="body">B-complex vitamins may help keep skin and blood cells healthy as well as convert nutrients into energy.</p>
  <p class="body ing" style="margin-top:24px">Calcium Chloride</p>
  <p class="body">&nbsp;Calcium helps promote healthy bones and the normal functioning of muscles, nerves and cells in the body.</p>
  <p class="body ing" style="margin-top:24px">Hydroxo B12</p>
  <p class="body">Hydroxo B12 is designed to help treat low levels of Vitamin B12, as well as promote healthy brain function, blood, cells and nerves.</p>
  <p class="body ing" style="margin-top:24px">Magnesium Chloride</p>
  <p class="body">Magnesium chloride can help improve immunity, decrease risk of developing migraines, improve relaxation and more.</p>
</div>
<div class="btn-book">BOOK NOW</div>

<div class="dots"><span></span><span class="on"></span><span></span><span></span><span></span><span></span><span></span><span></span></div>

<h2 class="section-title" style="top:1878px">OUR PACKAGES</h2>

<section class="packages">
  <div class="pkg">
    <svg width="70" height="62" viewBox="0 0 70 62"><path d="M35 58 C10 40 3 28 3 18 A16 16 0 0 1 35 12 A16 16 0 0 1 67 18 C67 28 60 40 35 58Z" fill="none" stroke="#fff" stroke-width="2.5"/></svg>
    <h4>4 PACK IVS</h4>
    <ul><li>4 Pack - $500 includes:</li><li>Any four IV Infusions</li><li>Regular price $175 ea</li><li>Total Package Value &nbsp;&nbsp;&nbsp;$700 ($200 savings)</li><li>Your price &nbsp;$125 each</li></ul>
    <div class="link">Book Now &nbsp;&nbsp;&nbsp;&rarr;</div>
  </div>
  <div class="pkg featured">
    <svg width="80" height="80" viewBox="0 0 80 80"><circle cx="40" cy="40" r="36" fill="none" stroke="#fff" stroke-width="3"/><path d="M40 20V60M20 40H60" stroke="#fff" stroke-width="8"/></svg>
    <h4>12 PACK IVS</h4>
    <ul><li>2 Pack - $1200 includes:</li><li>Any twelve IV Infusions</li><li>Regular price $175 ea</li><li style="line-height:20px">Total Package Value &nbsp;&nbsp;&nbsp;$2100 ($900 savings)</li></ul>
    <div class="link" style="bottom:62px">Book Now &nbsp;&nbsp;&nbsp;&rarr;</div>
  </div>
  <div class="pkg">
    <svg width="50" height="62" viewBox="0 0 50 62"><path d="M25 4 C14 22 8 32 8 42 A17 17 0 0 0 42 42 C42 32 36 22 25 4Z" fill="none" stroke="#fff" stroke-width="2.5"/></svg>
    <h4>6 PACK IVS</h4>
    <ul><li>4 Pack - $500 includes:</li><li>Any four IV Infusions</li><li>Regular price $175 ea</li><li style="line-height:20px">Total Package Value &nbsp;&nbsp;&nbsp;$700 ($200 savings)</li><li>Your price &nbsp;$125 each</li></ul>
    <div class="link" style="bottom:28px">Book Now &nbsp;&nbsp;&nbsp;&rarr;</div>
  </div>
</section>

<h2 class="section-title care-title">TAKING CARE OF YOUR HEALTH</h2>
<p class="care-intro">Services offered from Comprehensive exams to sports and physicals, Men's Health, Medical Cannabis Certifications, &nbsp;Hormonal Therapy, Testosterone and B12 supplementation, Immigration Exams, and many other services. Bilingual (Spanish and English).</p>

<div class="service" style="left:153px;top:2715px">
  <svg width="50" height="70" viewBox="0 0 50 70"><rect x="10" y="4" width="30" height="40" rx="10" fill="var(--teal)"/><path d="M25 44V66" stroke="var(--teal)" stroke-width="4"/><circle cx="25" cy="24" r="4" fill="#fff"/></svg>
  <h5>IV Nutrition Therapy</h5>
  <p>Direct infusion of vitamins and minerals, like high doses of vitamin C or magnesium.</p>
</div>
<div class="service" style="left:479px;top:2715px">
  <svg width="60" height="70" viewBox="0 0 60 70"><path d="M23 4H37M26 4V28L8 64H52L34 28V4" fill="none" stroke="var(--teal)" stroke-width="4"/><path d="M16 48H44L52 64H8Z" fill="var(--teal)"/></svg>
  <h5>Lab Services</h5>
  <p>We provide our clients with access to over 6000 individual tests, test panels.</p>
</div>
<div class="service" style="left:804px;top:2700px">
  <svg width="66" height="88" viewBox="0 0 66 88"><rect x="4" y="8" width="58" height="76" rx="8" fill="none" stroke="var(--teal)" stroke-width="4"/><rect x="20" y="3" width="26" height="12" rx="3" fill="var(--teal)"/><path d="M33 26V40M26 33H40M16 54H50M16 63H50M16 72H50" stroke="var(--teal)" stroke-width="3"/></svg>
  <h5 style="margin-top:0">Health Report</h5>
  <p>Reports convert standard lab results to uncover dysfunction areas from a functional health perspective.</p>
</div>

<div class="service" style="left:153px;top:3048px">
  <svg width="74" height="80" viewBox="0 0 74 80"><circle cx="37" cy="38" r="32" fill="none" stroke="var(--teal)" stroke-width="1.5"/><path d="M28 72V44L26 28M36 72V40L34 22M44 72V46L46 30" fill="none" stroke="var(--teal)" stroke-width="1.5"/></svg>
  <h5>Veriscan Bioscan</h5>
  <p>Veriscan helps you design a personalized health and nutrition program specific to your body's needs.</p>
</div>
<div class="service" style="left:479px;top:3040px">
  <svg width="90" height="90" viewBox="0 0 90 90"><circle cx="45" cy="45" r="16" fill="none" stroke="var(--teal)" stroke-width="6"/><g stroke="var(--teal)" stroke-width="6"><path d="M45 4V24M45 66V86M4 45H24M66 45H86M16 16L30 30M60 60L74 74M74 16L60 30M30 60L16 74"/></g></svg>
  <h5 style="margin-top:8px">Lumen-Laser Therapy</h5>
  <p>Class IV Laser manages pain and inflammation while accelerating tissue regeneration</p>
</div>
<div class="service" style="left:804px;top:3052px">
  <svg width="70" height="70" viewBox="0 0 70 70"><path d="M35 4L64 20V50L35 66L6 50V20Z M35 4L22 36L35 66L48 36Z M6 20L22 36L6 50 M64 20L48 36L64 50 M22 36H48" fill="none" stroke="var(--teal)" stroke-width="1.5"/></svg>
  <h5>Pulsara 200</h5>
  <p style="margin-top:36px">Deep Oscillation Therapy for muscle relaxation, pain relief, and increasing circulation.</p>
</div>

<div class="service" style="left:153px;top:3384px">
  <svg width="50" height="82" viewBox="0 0 50 82"><path d="M8 4H42V28A17 17 0 0 1 8 28Z" fill="var(--teal)"/><path d="M25 44V78M12 78H38" stroke="var(--teal)" stroke-width="4"/></svg>
  <h5 class="linked">Chinese Cupping</h5>
  <p>Helps with pain, inflammation, blood flow, relaxation and well-being, and as a type of deep-tissue massage.</p>
</div>
<div class="service" style="left:479px;top:3384px">
  <svg width="96" height="82" viewBox="0 0 96 82"><path d="M18 40V12A8 8 0 0 1 34 12V16" fill="none" stroke="var(--teal)" stroke-width="3"/><path d="M4 42H92V52A20 20 0 0 1 72 72H24A20 20 0 0 1 4 52Z" fill="none" stroke="var(--teal)" stroke-width="3"/><path d="M22 72L18 80M74 72L78 80" stroke="var(--teal)" stroke-width="3"/></svg>
  <h5 class="linked">Detox Footbath</h5>
  <p>Improve your health through cellular detoxification with the Ionfresh Detox Footbath from Clearwave Labs.</p>
</div>
<div class="service" style="left:804px;top:3412px">
  <svg width="70" height="44" viewBox="0 0 70 44"><path d="M8 8L24 4L28 20L16 30Z" fill="#8ab0c4"/><path d="M40 14L56 6L66 22L54 42L40 34Z" fill="var(--teal)"/></svg>
  <h5>Crystal Bath</h5>
  <p style="margin-top:32px">Seven clear and highly polished Lindqvist cut quartz crystals cleanse, balance, and align your energies.</p>
</div>

<div class="service" style="left:153px;top:3646px">
  <svg width="80" height="56" viewBox="0 0 80 56"><path d="M8 14L70 46L64 54L2 22Z" fill="var(--teal)"/><path d="M8 14L20 20L14 30L2 22Z" fill="#cfe6ec"/></svg>
  <h5 class="linked">Smoking Cessation Program</h5>
  <p style="margin-top:22px">This program provides more than the standard treatment for nicotine dependence, it offers a complete, integrative medical approach to treating your tobacco dependence addressing all aspects - mind, body &amp; spirit.</p>
</div>

<section class="newsletter">
  <h2>NEVER MISS AN UPDATE</h2>
  <div class="email-field">ENTER YOUR EMAIL HERE</div>
  <div class="join-btn">JOIN OUR MAILING LIST</div>
</section>

<footer class="site-footer">
  <div class="footer-col" style="left:92px;top:62px">CALL US<br>555.014.2276</div>
  <div class="footer-rule" style="left:339px"></div>
  <div class="footer-col" style="left:402px;top:68px">EMAIL US<br>hello@maplecrestdripcare.com</div>
  <div class="footer-rule" style="left:753px"></div>
  <div class="footer-col" style="left:818px;top:42px">LOCATION<br>2140 Birchwood Commons Blvd.<br>Maplecrest, FL 32900</div>
</footer>

</body>
</html>
```